New business card/stationary for a consulting company

I am looking for a clean and very professional looking business card for my consulting company as well as corresponding stationary. I am uploading our logo. I like simple and powerful for the feel. No graphics but I am open on everything else. Below is my contact information but would like the final to be in a version I can add my employees information into and print. Thank you.

Daniel Whitcombe
dan@fernlowadvisory.com
2837 North 9th Avenue, Summit Floor, Elm Crest, Indiana 60483
www.fernlowadvisory.com

Industry/Entity Type

Consulting

Contact Information for Business Card

Daniel Whitcombe
dan@fernlowadvisory.com
www.fernlowadvisory.com

Font styles to use
Serif
Sans Serif

Requirements
Must have
• Our logo and the business card details.
Nice to have
• our website www.fernlowadvisory.com

```html
<!DOCTYPE html>
<html lang="en">
<head>
<meta charset="utf-8">
<title>Fernlow Advisory – Business Card</title>
<link rel="stylesheet" href="https://fonts.googleapis.com/css2?family=Questrial&family=Lora:wght@400;700&display=swap">
<style>
  :root{
    --stage-light:#5a5a5a;
    --stage-dark:#111111;
    --brand-blue:#0a0c9c;
    --brand-blue-deep:#05066a;
    --navy-ink:#0b0f6e;
    --paper:#f4f4f4;
    --paper-shade:#dcdcdc;
    --body-ink:#1a1a1a;
    --white:#ffffff;
  }
  *{box-sizing:border-box;margin:0;padding:0}
  html,body{width:1200px;height:1090px;overflow:hidden}
  body{
    background:radial-gradient(ellipse at 55% 40%,var(--stage-light) 0%,#2c2c2c 45%,var(--stage-dark) 100%);
    position:relative;
    font-family:"Lora",serif;
  }
  .card{
    position:absolute;left:250px;width:700px;height:400px;
    border-radius:26px;overflow:hidden;
    box-shadow:0 18px 40px rgba(0,0,0,.55);
  }
  /* back side */
  .card-back{
    top:70px;
    background:radial-gradient(ellipse at 50% 45%,var(--brand-blue) 0%,var(--brand-blue-deep) 100%);
    color:var(--white);
  }
  .card-back .brand{
    position:absolute;left:0;right:0;top:130px;
    display:flex;align-items:center;justify-content:center;gap:22px;
  }
  .brand-square{width:56px;height:56px;background:var(--white);flex:none}
  .brand-name{
    font-family:"Questrial",sans-serif;font-weight:400;
    letter-spacing:.06em;white-space:nowrap;
  }
  .card-back .brand-name{font-size:46px;color:var(--white)}
  .card-back .website{
    position:absolute;left:0;right:0;top:232px;text-align:center;
    font-size:22px;letter-spacing:.02em;
  }
  .card-back .rule{
    position:absolute;left:0;right:0;top:330px;height:2px;background:var(--white);opacity:.9;
  }
  /* front side */
  .card-front{
    top:610px;
    background:linear-gradient(160deg,var(--paper) 0%,var(--white) 40%,var(--paper-shade) 100%);
  }
  .band{
    position:absolute;left:0;right:0;top:0;height:118px;
    background:radial-gradient(ellipse at 55% 100%,var(--brand-blue) 0%,var(--brand-blue-deep) 100%);
  }
  .band .brand{
    position:absolute;right:36px;top:0;height:118px;
    display:flex;align-items:center;gap:14px;
  }
  .band .brand-square{width:40px;height:40px}
  .band .brand-name{font-size:31px;color:var(--white)}
  .person{position:absolute;left:48px;top:150px}
  .person-name{
    font-weight:700;font-size:27px;color:var(--navy-ink);
    letter-spacing:.02em;text-transform:uppercase;margin-bottom:14px;
  }
  .contact-line{
    display:flex;align-items:center;gap:12px;
    font-size:19px;color:var(--body-ink);margin-bottom:8px;
  }
  .icon{width:26px;height:24px;flex:none}
  .address{
    position:absolute;left:300px;top:280px;
    display:flex;gap:12px;font-size:19px;line-height:1.45;color:var(--body-ink);
  }
</style>
</head>
<body>

<section class="card card-back" aria-label="Business card back">
  <div class="brand">
    <span class="brand-square" aria-hidden="true"></span>
    <span class="brand-name">FERNLOW ADVISORY</span>
  </div>
  <p class="website">www.fernlowadvisory.com</p>
  <div class="rule"></div>
</section>

<section class="card card-front" aria-label="Business card front">
  <div class="band">
    <div class="brand">
      <span class="brand-square" aria-hidden="true"></span>
      <span class="brand-name">FERNLOW ADVISORY</span>
    </div>
  </div>

  <div class="person">
    <h1 class="person-name">Daniel Whitcombe</h1>
    <p class="contact-line">
      <svg class="icon" viewBox="0 0 26 24" aria-hidden="true">
        <rect width="26" height="24" fill="#0b0f6e"/>
        <rect x="6" y="7" width="14" height="10" fill="none" stroke="#fff" stroke-width="1.5"/>
        <path d="M6 7l7 6 7-6" fill="none" stroke="#fff" stroke-width="1.5"/>
      </svg>
      dan@fernlowadvisory.com
    </p>
    <p class="contact-line">
      <svg class="icon" viewBox="0 0 26 24" aria-hidden="true">
        <rect width="26" height="24" fill="#0b0f6e"/>
        <circle cx="13" cy="12" r="6.5" fill="none" stroke="#fff" stroke-width="1.5"/>
        <path d="M6.5 12h13M13 5.5c-3 3.5-3 9.5 0 13M13 5.5c3 3.5 3 9.5 0 13" fill="none" stroke="#fff" stroke-width="1.2"/>
      </svg>
      www.fernlowadvisory.com
    </p>
  </div>

  <div class="address">
    <svg class="icon" viewBox="0 0 26 24" aria-hidden="true">
      <rect width="26" height="24" fill="#0b0f6e"/>
      <path d="M13 20s-5-5.5-5-9a5 5 0 0 1 10 0c0 3.5-5 9-5 9z" fill="#fff"/>
      <circle cx="13" cy="11" r="2" fill="#0b0f6e"/>
    </svg>
    <p>2837 North 9th Avenue, Summit Floor,<br>Elm Crest, Indiana 60483</p>
  </div>
</section>

</body>
</html>
```